Business Card Design Project

We have a logo, but would like to expand the use of it into a business card design. We are a B2B technology exchange platform for institutional investors to invest excess cash into short term assets matching their credit and pricing parameters. The assets are fractionalized and investors invest in portions.

Our customers are large, institutional, financial companies who are a bit traditional. We are high energy rebels with a cause...we are a disruptive technology and want to be viewed as a game changer but we need to present an image of trustworthiness and secure.

We are open not only to the image design but the material, die cut, etc. but want to stay in the traditional size of a business card.

We have other formats of the logo if needed. Our website is www.brambleharbor.com
Updates

I have posted a powerpoint template that we have been using.  This should not be considered the template we will use (after business cards we will have another project to incorporate business card design into powerpoint template) but just to give you a flavor of where we have been and have used in the past.

Target Market(s)

Institutional investors, asset managers, large fund institutions

Industry/Entity Type

Financial

Requirements
Must have
• Our logo
Traditional size
Nice to have
• unique use of logo, unique material, die cut, etc
Crisp, clean look
Use of both sides of card in a creative manner

```html
<!DOCTYPE html>
<html lang="en">
<head>
<meta charset="utf-8">
<title>Bramble Harbor Business Card</title>
<link href="https://fonts.googleapis.com/css2?family=Montserrat:wght@700&family=Open+Sans:wght@400;600&display=swap" rel="stylesheet">
<style>
  :root {
    --stage: #e6e6e6;
    --orange: #f07a14;
    --orange-deep: #e35d0a;
    --orange-light: #f7a03a;
    --charcoal: #2a2a2a;
    --charcoal-mid: #3a3a3a;
    --slate: #4a4a4a;
    --panel: #f4f4f4;
    --ink: #55565a;
    --white: #ffffff;
    --muted: #e2e2e2;
  }
  * { box-sizing: border-box; margin: 0; padding: 0; }
  html, body { width: 1200px; height: 861px; overflow: hidden; }
  body {
    background: var(--stage);
    font-family: "Open Sans", Arial, sans-serif;
    position: relative;
  }
  .card {
    position: absolute;
    width: 500px;
    height: 286px;
    border-radius: 4px;
    overflow: hidden;
    box-shadow: 0 6px 18px rgba(0,0,0,.18);
  }

  /* Front */
  .card--front {
    left: 350px; top: 70px;
    background: linear-gradient(160deg, var(--charcoal-mid) 0%, var(--charcoal) 60%, #1f1f1f 100%);
  }
  .front__top-panel {
    position: absolute; left: 0; top: 0; width: 100%; height: 60px;
    background: var(--panel);
  }
  .front__band {
    position: absolute; left: 0; top: 60px; width: 100%; height: 20px;
    background: linear-gradient(90deg, var(--orange-deep), var(--orange-light));
  }
  .front__logo-panel {
    position: absolute; right: 0; top: 0; width: 240px; height: 168px;
    background: var(--panel);
    border-bottom-left-radius: 18px;
    box-shadow: -4px 4px 0 var(--orange);
  }
  .front__brand {
    position: absolute; right: 0; top: 0; width: 240px; height: 168px;
    display: flex; align-items: center; justify-content: center; gap: 10px;
    padding-top: 14px;
  }
  .front__brand-name {
    font-family: "Montserrat", Arial, sans-serif; font-weight: 700;
    font-size: 28px; line-height: 1.05; color: var(--ink); letter-spacing: .5px;
  }
  .front__brand-dot {
    width: 16px; height: 16px; border-radius: 50%;
    background: var(--orange); flex: none;
  }
  .contact {
    position: absolute; left: 20px; top: 98px; width: 220px;
    list-style: none; color: var(--muted); font-size: 11px; line-height: 1.35;
  }
  .contact__item { display: flex; align-items: flex-start; gap: 8px; margin-bottom: 3px; white-space: nowrap; }
  .contact__icon { width: 14px; height: 14px; flex: none; margin-top: 1px; }
  .person {
    position: absolute; right: 24px; bottom: 40px; width: 200px; text-align: left; color: var(--white);
  }
  .person__name {
    font-family: "Montserrat", Arial, sans-serif; font-weight: 700; font-size: 24px; line-height: 1.1;
  }
  .person__title {
    font-family: "Open Sans", Arial, sans-serif; font-weight: 600; font-size: 13px; margin-top: 2px;
  }

  /* Backs */
  .card--back-orange {
    left: 80px; top: 460px;
    background: radial-gradient(circle at 35% 70%, var(--orange-deep) 0%, var(--orange) 45%, var(--orange-light) 100%);
  }
  .card--back-dark {
    left: 620px; top: 460px;
    background: radial-gradient(circle at 30% 75%, var(--slate) 0%, var(--charcoal-mid) 50%, var(--charcoal) 100%);
  }
  .back__brand {
    position: absolute; left: 0; right: 0; top: 112px; text-align: center;
    font-family: "Montserrat", Arial, sans-serif; font-weight: 700;
    font-size: 34px; color: var(--white); letter-spacing: 1px;
  }
  .back__web {
    position: absolute; left: 0; right: 0; top: 178px; text-align: center;
    font-family: "Montserrat", Arial, sans-serif; font-weight: 700;
    font-size: 20px; color: var(--white);
  }
</style>
</head>
<body>

  <section class="card card--front" aria-label="Card front">
    <div class="front__top-panel"></div>
    <div class="front__band"></div>
    <div class="front__logo-panel"></div>
    <div class="front__brand">
      <span class="front__brand-name">BRAMBLE<br>HARBOR</span>
      <span class="front__brand-dot"></span>
    </div>

    <ul class="contact">
      <li class="contact__item">
        <svg class="contact__icon" viewBox="0 0 14 14"><circle cx="7" cy="7" r="7" fill="#e2e2e2"/><path d="M7 3a2.6 2.6 0 0 0-2.6 2.6C4.4 7.6 7 11 7 11s2.6-3.4 2.6-5.4A2.6 2.6 0 0 0 7 3z" fill="#2a2a2a"/><circle cx="7" cy="5.6" r="1" fill="#e2e2e2"/></svg>
        <span>1820 Orchard Crest Road<br>Suite 410 Fernhill Village<br>CA 90210</span>
      </li>
      <li class="contact__item">
        <svg class="contact__icon" viewBox="0 0 14 14"><circle cx="7" cy="7" r="7" fill="#e2e2e2"/><path d="M4.6 3.8l1.3-.3.8 1.9-.9.7a5 5 0 0 0 2.1 2.1l.7-.9 1.9.8-.3 1.3c-3 .3-5.9-2.6-5.6-5.6z" fill="#2a2a2a"/></svg>
        <span>555.210.4418</span>
      </li>
      <li class="contact__item">
        <svg class="contact__icon" viewBox="0 0 14 14"><circle cx="7" cy="7" r="7" fill="#e2e2e2"/><rect x="5" y="3.2" width="4" height="7.6" rx=".8" fill="#2a2a2a"/><rect x="5.7" y="4.2" width="2.6" height="4.6" fill="#e2e2e2"/></svg>
        <span>555.310.7702</span>
      </li>
      <li class="contact__item">
        <svg class="contact__icon" viewBox="0 0 14 14"><circle cx="7" cy="7" r="7" fill="#e2e2e2"/><rect x="3.6" y="4.6" width="6.8" height="4.8" fill="#2a2a2a"/><path d="M3.8 4.8L7 7.3l3.2-2.5" stroke="#e2e2e2" stroke-width=".8" fill="none"/></svg>
        <span>marcusellery@brambleharbor.com</span>
      </li>
      <li class="contact__item">
        <svg class="contact__icon" viewBox="0 0 14 14"><circle cx="7" cy="7" r="7" fill="#e2e2e2"/></svg>
        <span>profile.marcusellery</span>
      </li>
      <li class="contact__item">
        <svg class="contact__icon" viewBox="0 0 14 14"><circle cx="7" cy="7" r="7" fill="#e2e2e2"/><circle cx="7" cy="7" r="3.8" fill="none" stroke="#2a2a2a" stroke-width=".9"/><ellipse cx="7" cy="7" rx="1.6" ry="3.8" fill="none" stroke="#2a2a2a" stroke-width=".8"/><path d="M3.2 7h7.6" stroke="#2a2a2a" stroke-width=".8"/></svg>
        <span>www.BrambleHarbor.com</span>
      </li>
    </ul>

    <div class="person">
      <h1 class="person__name">Marcus Ellery</h1>
      <p class="person__title">President &amp; CEO</p>
    </div>
  </section>

  <section class="card card--back-orange" aria-label="Card back, orange">
    <div class="back__brand">BRAMBLE HARBOR</div>
  </section>

  <section class="card card--back-dark" aria-label="Card back, charcoal">
    <div class="back__brand">BRAMBLE HARBOR</div>
    <div class="back__web">www.brambleharbor.com</div>
  </section>

</body>
</html>
```